Dog grooming business card
This is a business card for m dog grooming business like it say above.
In the priorities box below I will have the text that I want on the card.

Industry/Entity Type

Business

Colors

Designer to choose colors to be used in the design.

Requirements
Must have
• My logo and the insurance stamp must be on the card.

Text it must have :

Professional grooming services
Email: lindomerfield@brightmail.example
Text or call 1 705 318 6052
KSR certified/member
Pet first aid certified
Next appointment ___________________________________
Nice to have
• Greens to match my logo

```html
<!DOCTYPE html>
<html lang="en">
<head>
<meta charset="utf-8">
<title>Lindo Merfield – Grooming Business Card</title>
<link rel="stylesheet" href="https://fonts.googleapis.com/css2?family=Fira+Sans:wght@700&family=Fira+Sans+Condensed:wght@300;400&family=Lobster&display=swap">
<style>
  :root {
    --page: #ffffff;
    --card: #ffffff;
    --card-edge: #e4e4e4;
    --ink: #1f1f1f;
    --green: #8cc63f;
    --green-line: #7fae3a;
    --green-dark: #3d5a16;
    --badge-blue: #2a6db5;
  }
  * { margin: 0; padding: 0; box-sizing: border-box; }
  html, body { width: 1200px; height: 925px; overflow: hidden; background: var(--page); }
  .canvas { position: relative; width: 1200px; height: 925px; }

  .card {
    position: absolute; top: 52px; width: 464px; height: 806px;
    background: var(--card); border: 1px solid var(--card-edge);
    color: var(--ink);
  }
  .card--front { left: 100px; }
  .card--back { left: 620px; }

  /* Front */
  .brand-dot {
    position: absolute; left: 152px; top: 40px; width: 160px; height: 160px;
    border-radius: 50%; background: var(--green);
  }
  .brand-name {
    position: absolute; left: 0; right: 0; top: 200px; text-align: center;
    font-family: "Lobster", cursive; font-size: 56px; color: var(--green-dark); line-height: 1;
  }
  .tagline {
    position: absolute; left: 0; right: 0; top: 356px; text-align: center;
    font-family: "Fira Sans", sans-serif; font-weight: 700; font-size: 26px; line-height: 35px;
  }
  .contact {
    position: absolute; left: 0; right: 0; top: 460px; text-align: center; list-style: none;
    font-family: "Fira Sans Condensed", sans-serif; font-weight: 300; font-size: 25px; line-height: 35.5px;
  }
  .flourish {
    position: absolute; left: 37px; top: 690px; width: 390px; height: 62px;
    background: linear-gradient(90deg, rgba(127,174,58,0.15), rgba(127,174,58,0.55), rgba(127,174,58,0.15));
    border-radius: 30px;
  }

  /* Back */
  .reminder-title {
    position: absolute; left: 0; right: 0; top: 66px; text-align: center;
    font-family: "Lobster", cursive; font-size: 40px; font-weight: 400;
  }
  .rule { position: absolute; left: 0; width: 464px; height: 10px; }
  .rule path { fill: none; stroke: var(--green-line); stroke-width: 1.6; }

  .weekdays, .dates, .months {
    position: absolute; font-family: "Fira Sans", sans-serif; font-weight: 700; list-style: none;
  }
  .weekdays {
    left: 40px; right: 40px; top: 174px; display: flex; justify-content: space-between; font-size: 26px;
  }
  .dates {
    left: 33px; top: 264px; display: grid; grid-template-columns: repeat(7, 57px);
    grid-auto-rows: 48px; font-size: 26px; text-align: center;
  }
  .months {
    left: 33px; top: 550px; display: grid; grid-template-columns: repeat(6, 66.6px);
    grid-auto-rows: 42px; font-size: 21px; text-align: center;
  }
  .appointment-time {
    position: absolute; left: 35px; top: 696px;
    font-family: "Fira Sans Condensed", sans-serif; font-weight: 300; font-size: 25px;
  }
  .insurance-badge {
    position: absolute; left: 332px; top: 688px; width: 94px; height: 48px;
    border: 1.5px solid var(--badge-blue); border-radius: 8px; background: #fff;
  }
</style>
</head>
<body>
<main class="canvas">
  <section class="card card--front" aria-label="Business card front">
    <div class="brand-dot"></div>
    <h1 class="brand-name">Lindo Merfield</h1>
    <p class="tagline">Professional grooming<br>services</p>
    <ul class="contact">
      <li>lindomerfield@brightmail.example</li>
      <li>Text or call: 1 705 318 6052</li>
      <li>KSR certified/member</li>
      <li>Pet first aid certified</li>
    </ul>
    <div class="flourish" role="img" aria-label="Green decorative scroll flourish"></div>
  </section>

  <section class="card card--back" aria-label="Appointment reminder card back">
    <h2 class="reminder-title">Appointment reminder</h2>
    <svg class="rule" style="top:140px" viewBox="0 0 464 10"><path d="M0 6 Q232 -2 464 6"/></svg>
    <ul class="weekdays"><li>MON</li><li>TUE</li><li>WEDS</li><li>THURS</li><li>FRI</li></ul>
    <svg class="rule" style="top:223px" viewBox="0 0 464 10"><path d="M0 6 Q232 -2 464 6"/></svg>
    <ol class="dates">
      <li>1</li><li>2</li><li>3</li><li>4</li><li>5</li><li>6</li><li>7</li>
      <li>8</li><li>9</li><li>10</li><li>11</li><li>12</li><li>13</li><li>14</li>
      <li>15</li><li>16</li><li>17</li><li>18</li><li>19</li><li>20</li><li>21</li>
      <li>22</li><li>23</li><li>24</li><li>25</li><li>26</li><li>27</li><li>28</li>
      <li>29</li><li>30</li><li>31</li>
    </ol>
    <svg class="rule" style="top:518px" viewBox="0 0 464 10"><path d="M0 6 Q232 -2 464 6"/></svg>
    <ul class="months">
      <li>JAN</li><li>FEB</li><li>MAR</li><li>APR</li><li>MAY</li><li>JUN</li>
      <li>JUL</li><li>AUG</li><li>SEP</li><li>OCT</li><li>NOV</li><li>DEC</li>
    </ul>
    <svg class="rule" style="top:640px" viewBox="0 0 464 10"><path d="M0 6 Q232 -2 464 6"/></svg>
    <p class="appointment-time">At ______ : ______am/pm</p>
    <div class="insurance-badge" role="img" aria-label="Insurance protection stamp"></div>
  </section>
</main>
</body>
</html>
```